Beef cattle farm needs signs which can be seen from roadside

We would like submissions of artwork for a sign that will hang from a fence or gate and will be seen by passing cars.

Existing logo and branding theme for the company is attached.

Signage can be between 900mm x 400mm - 1200mm x 600mm

Industry/Entity Type

Farm

Requirements
Must have
• the Signs should have the following information:
• Company name: Brindle Ridge Grazing Company
• Address: 214 Wattlebank Hollow Road
• Contact number: 0431 862 475
• email address: admin@brindleridgegrazingco.com.au
• - Logo and branding as per attached artwork

```html
<!DOCTYPE html>
<html lang="en">
<head>
<meta charset="utf-8">
<title>Brindle Ridge Grazing Company – Roadside Sign</title>
<link rel="stylesheet" href="https://fonts.googleapis.com/css2?family=Archivo+Black&family=Mada:wght@600&family=Montserrat:wght@500&display=swap">
<style>
  :root {
    --canvas-bg: #ffffff;
    --brand-green: #206f47;
    --sign-black: #000000;
    --contact-green: #1ea85a;
    --text-white: #ffffff;
  }
  html, body {
    margin: 0;
    padding: 0;
    width: 1200px;
    height: 1000px;
    overflow: hidden;
    background: var(--canvas-bg);
  }
  .canvas {
    position: relative;
    width: 1200px;
    height: 1000px;
  }
  .sign {
    position: absolute;
    left: 150px;
    top: 300px;
    width: 900px;
    height: 400px;
    display: flex;
  }
  .brand-panel {
    width: 315px;
    height: 100%;
    background: var(--brand-green);
    display: flex;
    flex-direction: column;
    align-items: center;
    justify-content: center;
    gap: 22px;
  }
  .brand-dot {
    width: 150px;
    height: 150px;
    border-radius: 50%;
    background: var(--text-white);
  }
  .brand-name {
    margin: 0;
    font-family: "Montserrat", sans-serif;
    font-weight: 500;
    font-size: 25px;
    line-height: 1.25;
    letter-spacing: 1px;
    text-transform: uppercase;
    text-align: center;
    color: var(--text-white);
  }
  .contact-panel {
    flex: 1;
    height: 100%;
    background: var(--sign-black);
    display: flex;
    flex-direction: column;
    align-items: center;
    padding-top: 62px;
    box-sizing: border-box;
  }
  .contact-heading {
    margin: 0 0 30px;
    font-family: "Archivo Black", sans-serif;
    font-size: 50px;
    line-height: 1;
    color: var(--text-white);
    letter-spacing: -0.5px;
  }
  .contact-line {
    margin: 0;
    font-family: "Mada", sans-serif;
    font-weight: 600;
    color: var(--contact-green);
    text-align: center;
    line-height: 1.2;
  }
  .contact-address { font-size: 44px; }
  .contact-phone { font-size: 44px; margin-top: 6px; }
  .contact-email { font-size: 26px; margin-top: 10px; }
</style>
</head>
<body>
  <div class="canvas">
    <div class="sign">
      <div class="brand-panel">
        <div class="brand-dot"></div>
        <p class="brand-name">Brindle Ridge<br>Grazing Company</p>
      </div>
      <div class="contact-panel">
        <h1 class="contact-heading">CONTACT US :</h1>
        <p class="contact-line contact-address">214 Wattlebank Hollow Road</p>
        <p class="contact-line contact-phone">0431 862 475</p>
        <p class="contact-line contact-email">admin@brindleridgegrazingco.com.au</p>
      </div>
    </div>
  </div>
</body>
</html>
```